Shopify Design for wedding invitations

We are a greeting card manufactory, special in wedding invitation
I need a shopify website for our wedding invitation brand. (Lovonna), atttach you can find our logo.
We are looking for someone to create a modern and clean looking e-commerce store for our wedding invitation through Shopify. We need some life, professionalism and style put into our site. We will have a variety serie of products : laser cut wedding invitation, popup wedding invitaiton, vintage wedding invitation, handmade wedding invitation, printing invitation, Custom wedding cards, wedding stationery (including favor box, table card, place card, escort card, number card), Thank you card. our online store requires easy navigation to categories divided by product type.

our market is , Eourpe and USA,
please choose a good color for it.
you can go to our website: www.bluepinecrafts.com and check our product.
also you can go to Shopvane 4 new items.
https://www.shopvane.com/dp/K47T8M2Q61?ref=myi_title_dp

Designs look the same

Target Market(s)

Europe and USA

Industry/Entity Type

wedding

Number of Pages Required

1 page

Requirements
Must have
• Logo, 3 banners than can be changed each 3-5 seconds.
Nice to have
• nice icon and font, beautiful color,

```html
<!DOCTYPE html>
<html lang="en">
<head>
<meta charset="utf-8">
<title>Lovonna – Wedding Invitations</title>
<link href="https://fonts.googleapis.com/css2?family=Lato:wght@400;700&family=Princess+Sofia&display=swap" rel="stylesheet">
<style>
:root{
  --green:#6e9a35;
  --green-dark:#5d8a29;
  --ink:#333;
  --text:#555;
  --muted:#777;
  --nav:#1e1e1e;
  --white:#fff;
  --line:#8ab04f;
}
*{box-sizing:border-box;margin:0;padding:0}
html,body{width:1200px;height:2883px;overflow:hidden;background:var(--white)}
body{position:relative;font-family:'Lato',sans-serif;color:var(--text)}
.abs{position:absolute}
.topbar{top:0;left:0;width:1200px;height:27px;font-size:13px;font-weight:700;color:var(--ink)}
.topbar .links{position:absolute;right:150px;top:5px;letter-spacing:.3px}
.topbar .cart{position:absolute;right:122px;top:4px}
.navbar{top:27px;left:0;width:1200px;height:75px;background:var(--nav)}
.brand{position:absolute;left:126px;top:22px;color:var(--white);font-size:30px;font-weight:400;letter-spacing:1px}
.menu{position:absolute;left:370px;top:27px;display:flex;gap:24px;font-size:13.5px;font-weight:700;color:var(--white)}
.menu .active{color:var(--green);border-bottom:2px solid var(--green);padding-bottom:6px}
.search{position:absolute;left:916px;top:22px;width:163px;height:27px;border-radius:14px;background:var(--white);font-size:11px;color:#aaa;padding:7px 10px}
.search svg{position:absolute;right:10px;top:8px}
.hero{top:102px;left:0;width:1200px;height:382px;background:linear-gradient(100deg,#a99a7d 0%,#d9cdb6 30%,#efe6d6 50%,#b8a68a 75%,#7d6c55 100%)}
.hero-title{position:absolute;left:137px;top:48px;font-family:'Princess Sofia',cursive;font-size:66px;color:var(--white)}
.hero-sub{position:absolute;left:148px;top:160px;width:380px;text-align:center;font-family:'Princess Sofia',cursive;font-size:33px;line-height:40px;color:var(--white)}
.section-title{left:0;width:1200px;text-align:center;font-family:'Princess Sofia',cursive;color:var(--green);font-size:50px}
.dots{left:124px;width:952px;border-top:3px dotted var(--line)}
.intro{left:125px;width:950px;font-size:18.5px;line-height:27px;color:var(--text)}
.card{width:186px;text-align:center}
.card .photo{width:186px;height:186px;border:2px solid var(--green);background:linear-gradient(135deg,#7a4528,#a0603a 55%,#6b3a22)}
.card .name{margin-top:14px;font-size:12px;font-weight:700;color:var(--muted)}
.card .kind{font-size:12px;color:var(--muted);margin-top:2px}
.card .price{font-size:12px;font-weight:700;color:var(--green);margin-top:6px}
.avatar{width:100px;height:100px;border-radius:50%;border:3px solid var(--green);background:linear-gradient(160deg,#8a9a84,#c9c1b2 60%,#5f5a4e)}
.person{text-align:center;font-size:19.5px;line-height:27px;color:var(--text)}
.person h3{font-size:32px;color:var(--green);font-weight:700;line-height:36px}
.chat-dots{display:flex;gap:30px;justify-content:center;margin-top:8px}
.chat-dots span{width:38px;height:38px;border-radius:50%}
.c1{background:#2dbd2d}.c2{background:#1aa3e0}
.field{left:123px;width:951px;border:3px dotted var(--line);border-radius:14px;font-size:27px;color:var(--muted);padding:12px 8px}
.field sup{font-size:18px}
.btn{left:123px;top:2456px;width:196px;height:49px;border:3px dotted #e9f1dd;outline:2px solid var(--green);background:var(--green);border-radius:10px;color:var(--white);font-weight:700;font-size:21px;text-align:center;line-height:43px}
.footer{left:0;top:2560px;width:1200px;height:323px;background:var(--green);color:var(--white)}
.scallop{position:absolute;top:0;left:0;width:1200px;height:14px;background:radial-gradient(circle at 50% 0,var(--white) 9px,transparent 10px) repeat-x;background-size:48px 14px}
.social{position:absolute;top:43px;left:124px;display:flex;gap:14px}
.social span{width:26px;height:26px;border-radius:50%;border:2px solid var(--white)}
.fcol{position:absolute;top:88px;font-size:13px;line-height:16px}
.fcol h4{font-size:16px;margin-bottom:20px}
.fcol svg{position:absolute;left:-30px;top:38px}
.fnav{position:absolute;top:264px;left:0;width:1200px;display:flex;justify-content:center;gap:24px;font-size:13.5px;font-weight:700}
.copy{position:absolute;top:298px;width:1200px;text-align:center;font-size:13px;font-weight:700}
.sidebar{left:1136px;top:347px;width:50px;background:var(--white);box-shadow:0 0 4px rgba(0,0,0,.2)}
.sidebar div{height:48px;border-bottom:1px solid #e6e6e6;text-align:center;font-size:8px;color:#444;padding-top:6px}
.sidebar i{display:block;width:16px;height:16px;border-radius:50%;margin:0 auto 3px}
</style>
</head>
<body>
<div class="abs topbar"><span class="links">Register &nbsp;&nbsp;/&nbsp;&nbsp; Login</span>
<svg class="cart" width="22" height="18" viewBox="0 0 22 18"><path d="M1 2h4l3 10h10l2-7H7" fill="none" stroke="#333" stroke-width="2"/><circle cx="9" cy="16" r="1.6" fill="#333"/><circle cx="17" cy="16" r="1.6" fill="#333"/></svg></div>

<header class="abs navbar">
  <div class="brand">Lovonna</div>
  <nav class="menu"><span class="active">HOME</span><span>PRODUCTS</span><span>NEWS</span><span>ABOUT US</span><span>CONTACT US</span><span>SEND INQUIRY</span></nav>
  <div class="search">Please Enter Keyword<svg width="10" height="10" viewBox="0 0 10 10"><circle cx="4" cy="4" r="3" fill="none" stroke="#222" stroke-width="1.6"/><path d="M6 6l3 3" stroke="#222" stroke-width="1.6"/></svg></div>
</header>

<section class="abs hero" role="img" aria-label="Soft sepia photo of a smiling bride with a veil">
  <div class="hero-title">Life Company</div>
  <div class="hero-sub">You are the most beautiful promise of my life</div>
</section>

<aside class="abs sidebar">
  <div><i style="background:#1a73e8"></i>Customer Service</div>
  <div><i style="background:#2dbd2d"></i>Chat</div>
  <div><i style="background:#1aa3e0"></i>Call</div>
  <div><i style="background:#2dbd2d"></i>Talk</div>
  <div><i style="background:#f08a24"></i>Share</div>
  <div><i style="background:#1a73e8;border-radius:3px"></i>Message</div>
  <div style="border:0"><svg width="14" height="14" viewBox="0 0 14 14"><path d="M2 1h10M7 13V4M3 8l4-4 4 4" fill="none" stroke="#444" stroke-width="1.5"/></svg><br>Top</div>
</aside>

<h2 class="abs section-title" style="top:520px;font-size:52px">Hangzhou Blue Pine Crafts Co., Ltd.</h2>
<div class="abs dots" style="top:597px"></div>
<p class="abs intro" style="top:616px">Our company is established in 2001, located in Hang Zhou, Zhejiang Province.We are an professional manufacturer and exporter that is concerned with the design, development and production manufacturing wedding invitation card, favor boxes and other gift items.</p>
<p class="abs intro" style="top:724px">Our company products all passed the CE, FSC and BSCI accreditation. We are able to provide high-quality products to customers from around the world, main market areas include Europe(Germany, UK, France, Italy), USA, Asian(Japan, Korea, India), South America. We have always been the most trusted partner of our customers.</p>

<h2 class="abs section-title" style="top:855px">New Products</h2>
<div class="abs dots" style="top:925px"></div>

<div class="abs card" style="left:227px;top:953px"><div class="photo" role="img" aria-label="Burgundy laser-cut invitation on wood"></div><div class="name">PRODUCT 1</div><div class="kind">Vintage wedding invitation</div><div class="price">US $ 0,81 - US $ 1.17</div></div>
<div class="abs card" style="left:417px;top:953px"><div class="photo" role="img" aria-label="Gold butterfly laser-cut invitation"></div><div class="name">PRODUCT 2</div><div class="kind">Vintage wedding invitation</div><div class="price">US $ 0,81 - US $ 1.17</div></div>
<div class="abs card" style="left:607px;top:953px"><div class="photo" role="img" aria-label="Navy lace invitation with kraft envelope"></div><div class="name">PRODUCT 3</div><div class="kind">Vintage wedding invitation</div><div class="price">US $ 0,81 - US $ 1.17</div></div>
<div class="abs card" style="left:796px;top:953px"><div class="photo" role="img" aria-label="Gold lace pocket invitation"></div><div class="name">PRODUCT 4</div><div class="kind">Vintage wedding invitation</div><div class="price">US $ 0,81 - US $ 1.17</div></div>
<div class="abs card" style="left:227px;top:1232px"><div class="photo" role="img" aria-label="Burgundy laser-cut invitation on wood"></div><div class="name">PRODUCT 5</div><div class="kind">Vintage wedding invitation</div><div class="price">US $ 0,81 - US $ 1.17</div></div>
<div class="abs card" style="left:417px;top:1232px"><div class="photo" role="img" aria-label="Gold butterfly laser-cut invitation"></div><div class="name">PRODUCT 6</div><div class="kind">Vintage wedding invitation</div><div class="price">US $ 0,81 - US $ 1.17</div></div>
<div class="abs card" style="left:607px;top:1232px"><div class="photo" role="img" aria-label="Navy lace invitation with kraft envelope"></div><div class="name">PRODUCT 7</div><div class="kind">Vintage wedding invitation</div><div class="price">US $ 0,81 - US $ 1.17</div></div>
<div class="abs card" style="left:796px;top:1232px"><div class="photo" role="img" aria-label="Gold lace pocket invitation"></div><div class="name">PRODUCT 8</div><div class="kind">Vintage wedding invitation</div><div class="price">US $ 0,81 - US $ 1.17</div></div>

<h2 class="abs section-title" style="top:1520px">Contact Us</h2>
<div class="abs dots" style="top:1591px;left:122px"></div>

<div class="abs avatar" style="left:125px;top:1636px" role="img" aria-label="Profile photo"></div>
<div class="abs person" style="left:240px;top:1620px;width:305px"><h3>Daniel</h3>E-mail: admin@bluepinecrafts.com<br>Mobile phone: +86 13800410275<br>TEL: +86 13800410275</div>
<div class="abs avatar" style="left:671px;top:1639px" role="img" aria-label="Profile photo"></div>
<div class="abs person" style="left:785px;top:1622px;width:290px"><h3>Nora</h3>E-mail: nora@bluepinecrafts.com<br>TEL: +86 18900736412</div>

<div class="abs avatar" style="left:127px;top:1788px" role="img" aria-label="Profile photo"></div>
<div class="abs person" style="left:240px;top:1772px;width:305px"><h3>Lena</h3>E-mail: lena@bluepinecrafts.com<br>TEL: +86 18700528391<div class="chat-dots"><span class="c1"></span><span class="c2"></span></div></div>
<div class="abs avatar" style="left:671px;top:1788px" role="img" aria-label="Profile photo"></div>
<div class="abs person" style="left:780px;top:1772px;width:300px"><h3>Willa</h3>E-mail: willa@bluepinecrafts.com<br>Mobile phone: +86 05716648201<br>TEL: +86 18600934715<div class="chat-dots" style="margin-top:16px"><span class="c1"></span><span class="c2"></span></div></div>

<div class="abs avatar" style="left:127px;top:1937px" role="img" aria-label="Profile photo"></div>
<div class="abs person" style="left:240px;top:1932px;width:292px"><h3>Amy</h3>E-mail: amy@blue-pine.com<br>TEL: +86 18900736412</div>

<h2 class="abs section-title" style="top:2070px">Send Message</h2>
<div class="abs field" style="top:2156px;height:66px"><sup>*</sup>Email</div>
<div class="abs field" style="top:2258px;height:172px"><sup>*</sup>Message Content</div>
<div class="abs btn">SEND MESSAGE</div>

<footer class="abs footer">
  <div class="scallop"></div>
  <div class="social"><span></span><span></span><span></span></div>
  <div class="fcol" style="left:153px"><h4>Address</h4>
    <svg width="20" height="24" viewBox="0 0 20 24"><path d="M10 22s-7-8-7-13a7 7 0 0114 0c0 5-7 13-7 13z" fill="none" stroke="#fff" stroke-width="1.8"/><circle cx="10" cy="9" r="2.5" fill="none" stroke="#fff" stroke-width="1.8"/></svg>
    Rm B112, 3rd Floor,<br>Linhe Building,<br>Qiaoxi Road, Hangzhou,<br>P.R. CHINA, 310005</div>
  <div class="fcol" style="left:403px"><h4>Telephone</h4>
    <svg width="24" height="24" viewBox="0 0 24 24"><path d="M5 3l4 4-2 3c2 3 4 5 7 7l3-2 4 4-3 3C10 21 3 14 2 6z" fill="none" stroke="#fff" stroke-width="1.6"/></svg>
    +86 13800410275<br>+86 18600934715<br>+86 18700528391<br>18900736412<br>+86 18900736412</div>
  <div class="fcol" style="left:659px"><h4>Mobile phone</h4>
    <svg width="18" height="26" viewBox="0 0 18 26"><rect x="2" y="1" width="14" height="24" rx="2" fill="none" stroke="#fff" stroke-width="1.8"/><path d="M7 21h4" stroke="#fff" stroke-width="1.8"/></svg>
    +86 13800410275<br>+86 05716648201</div>
  <div class="fcol" style="left:913px"><h4>E-mail</h4>
    <svg width="26" height="20" viewBox="0 0 26 20"><rect x="1" y="2" width="24" height="16" rx="2" fill="none" stroke="#fff" stroke-width="1.8"/><path d="M2 3l11 9 11-9" fill="none" stroke="#fff" stroke-width="1.8"/></svg>
    admin@bluepinecrafts.com<br>nora@bluepinecrafts.com<br>lena@bluepinecrafts.com<br>willa@bluepinecrafts.com<br>amy@blue-pine.com</div>
  <nav class="fnav"><span>HOME</span><span>PRODUCTS</span><span>NEWS</span><span>ABOUT US</span><span>CONTACT US</span><span>SEND INQUIRY</span><span>SITEMAP</span></nav>
  <div class="copy">2022 Hangzhou Blue Pine Crafts Co., ltd. (203502) All rights reserved</div>
</footer>
</body>
</html>
```